Book jacket for Harrowby

We need a book jacket design (hard cover front, back, spine, flaps; soft cover and eBook). for a social psychology book with the general cluelessness (being "out of it") of how people function both in their personal and social lives. This is the third book written by the author, a practicing psychiatrist, and the content centers on a single subject, people's lack of genuine emotional contact, their cluelessness with themselves and with current national and world events.
Updates

Need extra days to review

Target Market(s)

People who want to better understand the state the nation and world is in now, and what they can do about it.

Font styles to use
Serif
Sans Serif

Requirements
Must have
• Bold, eye-catching cover
Nice to have
• Like the idea of separating the title word (harrow by) to better emphasize the concept of lack of contact

```html
<!DOCTYPE html>
<html lang="en">
<head>
<meta charset="utf-8">
<title>Harrowby — Book Jacket</title>
<link href="https://fonts.googleapis.com/css2?family=Montserrat:wght@800&family=Cormorant+Garamond:wght@500&display=swap" rel="stylesheet">
<style>
  :root {
    --backdrop: #e3e3e0;
    --board: #2b2b2b;
    --board-edge: #1f1f1f;
    --band: #3a3a3a;
    --accent: #f2ee1c;
    --ink: #161616;
  }
  html, body {
    margin: 0;
    padding: 0;
    width: 848px;
    height: 1200px;
    overflow: hidden;
    background: var(--backdrop);
  }
  .jacket {
    position: relative;
    width: 848px;
    height: 1200px;
  }
  .front-cover {
    position: absolute;
    left: 110px;
    top: 230px;
    width: 500px;
    height: 730px;
    background: var(--board);
    border-left: 8px solid var(--board-edge);
    box-sizing: border-box;
  }
  .title {
    position: absolute;
    left: 0;
    right: 0;
    top: 180px;
    text-align: center;
    font-family: "Montserrat", sans-serif;
    font-weight: 800;
    letter-spacing: 8px;
  }
  .title-boxed {
    display: inline-block;
    background: var(--accent);
    color: var(--ink);
    font-size: 68px;
    line-height: 1;
    padding: 22px 14px 22px 24px;
  }
  .title-open {
    display: block;
    color: var(--accent);
    font-size: 80px;
    line-height: 1;
    margin-top: 22px;
    letter-spacing: 18px;
    padding-left: 18px;
  }
  .author-band {
    position: absolute;
    left: 0;
    right: 0;
    top: 630px;
    height: 32px;
    background: var(--band);
    display: flex;
    align-items: center;
    justify-content: center;
  }
  .author {
    font-family: "Cormorant Garamond", serif;
    font-weight: 500;
    color: var(--accent);
    font-size: 21px;
    letter-spacing: 4px;
  }
  .spine {
    position: absolute;
    left: 690px;
    top: 232px;
    width: 72px;
    height: 728px;
    background: var(--board);
    box-sizing: border-box;
    display: flex;
    justify-content: center;
    padding-top: 46px;
  }
  .spine-stack {
    writing-mode: vertical-rl;
    display: flex;
    align-items: center;
  }
  .spine-title {
    font-family: "Montserrat", sans-serif;
    font-weight: 800;
    font-size: 34px;
    letter-spacing: 8px;
  }
  .spine-title-boxed {
    background: var(--accent);
    color: var(--ink);
    padding: 12px 8px 8px;
  }
  .spine-title-open {
    color: var(--accent);
    padding-top: 12px;
  }
  .spine-author {
    font-family: "Cormorant Garamond", serif;
    font-weight: 500;
    color: var(--accent);
    font-size: 19px;
    letter-spacing: 4px;
    margin-top: 34px;
  }
</style>
</head>
<body>
<main class="jacket">
  <section class="front-cover">
    <h1 class="title">
      <span class="title-boxed">HARROW</span>
      <span class="title-open">BY</span>
    </h1>
    <div class="author-band">
      <span class="author">Martin Selwyn M.D.</span>
    </div>
  </section>
  <aside class="spine">
    <div class="spine-stack">
      <span class="spine-title spine-title-boxed">HARROW</span>
      <span class="spine-title spine-title-open">BY</span>
      <span class="spine-author">Martin Selwyn M.D.</span>
    </div>
  </aside>
</main>
</body>
</html>
```